Summit Grading a Masonry LLC business card

My current business card is very plain. it has my logo and contact information. I woud like something that stands out from the rest. please take a look at my website to see about my company.

Compayt Name - Summit Grading And Masonry
Owner - Martin Galloway
Business Address
Business Website - www.summitgradingandmasonry.example
Email - Summitgradingandmasonry@mailbox.example
Phone - 555-214-3867
Fax - 555-630-2719

Target Market(s)

Everyone age tang is 18 - 85

Industry/Entity Type

Business

Contact Information for Business Card

Nice and professional all in one.

Font styles to use
Serif
Other font styles liked:
• Up to you

Requirements
Must have
• All contact info. The design is up to you.
Nice to have
• All the contact info the design is up to you
Should not have
• I don't have any

```html
<!DOCTYPE html>
<html lang="en">
<head>
<meta charset="utf-8">
<title>Summit Grading &amp; Masonry LLC — Business Card</title>
<link href="https://fonts.googleapis.com/css2?family=Tinos:wght@400;700&display=swap" rel="stylesheet">
<style>
  :root {
    --backdrop: #3b3532;
    --card: #e6e6e6;
    --ink: #1c1c1c;
    --rule: #2a2a2a;
  }
  * { box-sizing: border-box; margin: 0; padding: 0; }
  html, body {
    width: 1200px; height: 780px; overflow: hidden;
    background: var(--backdrop);
    font-family: "Tinos", "Times New Roman", serif;
    color: var(--ink);
  }
  .sheet {
    position: relative; width: 1200px; height: 780px;
    display: flex; align-items: center; justify-content: center; gap: 60px;
  }
  .card {
    position: relative; width: 520px; height: 297px;
    background: var(--card);
    box-shadow: 0 10px 24px rgba(0,0,0,.45);
  }
  .card-frame { position: absolute; inset: 0; width: 100%; height: 100%; }
  .card-frame path { fill: none; stroke: var(--rule); }
  .card-content {
    position: absolute; inset: 0;
    display: flex; flex-direction: column; align-items: center; justify-content: center;
    text-align: center;
  }
  .company-name {
    font-weight: 700; text-transform: uppercase;
    font-size: 30px; line-height: 1.02; letter-spacing: .5px;
    color: var(--ink);
  }
  .card-back .card-content { justify-content: flex-start; padding-top: 38px; }
  .card-back .company-name { font-size: 27px; margin-bottom: 12px; }
  .owner-name { font-weight: 700; font-size: 18px; line-height: 1.1; }
  .owner-title { font-size: 13px; margin-bottom: 6px; }
  .contact-list { list-style: none; font-size: 14.5px; line-height: 1.3; }
  .contact-list b { font-weight: 700; }
</style>
</head>
<body>
  <main class="sheet">
    <section class="card card-front" aria-label="Card front">
      <svg class="card-frame" viewBox="0 0 520 297" aria-hidden="true">
        <path stroke-width="1.6" d="M28 14 H492 A14 14 0 0 0 506 28 V269 A14 14 0 0 0 492 283 H28 A14 14 0 0 0 14 269 V28 A14 14 0 0 0 28 14 Z"/>
        <path stroke-width="1" d="M33 19 H487 A14 14 0 0 0 501 33 V264 A14 14 0 0 0 487 278 H33 A14 14 0 0 0 19 264 V33 A14 14 0 0 0 33 19 Z"/>
      </svg>
      <div class="card-content">
        <h1 class="company-name">Summit Grading<br>&amp; Masonry LLC</h1>
      </div>
    </section>

    <section class="card card-back" aria-label="Card back">
      <svg class="card-frame" viewBox="0 0 520 297" aria-hidden="true">
        <path stroke-width="1.6" d="M28 14 H492 A14 14 0 0 0 506 28 V269 A14 14 0 0 0 492 283 H28 A14 14 0 0 0 14 269 V28 A14 14 0 0 0 28 14 Z"/>
        <path stroke-width="1" d="M33 19 H487 A14 14 0 0 0 501 33 V264 A14 14 0 0 0 487 278 H33 A14 14 0 0 0 19 264 V33 A14 14 0 0 0 33 19 Z"/>
      </svg>
      <div class="card-content">
        <h2 class="company-name">Summit Grading<br>&amp; Masonry LLC</h2>
        <p class="owner-name">Martin Galloway</p>
        <p class="owner-title">Owner</p>
        <ul class="contact-list">
          <li>PO BOX 123 your address, 2nd street london ,USA</li>
          <li><b>P:</b> 555-214-3867 | <b>F:</b> 555-630-2719</li>
          <li><b>E:</b> Summitgradingandmasonry@mailbox.example</li>
          <li>www.summitgradingandmasonry.example</li>
        </ul>
      </div>
    </section>
  </main>
</body>
</html>
```